Sol Rumbo Coaching Services

My info is
Darsie Quenell-Abaro
darsie@solrumbocoaching.example
solrumbocoaching.example
555-413-7082

you can play with order of items. I've never had a letterhead before. Thank you!

```html
<!DOCTYPE html>
<html lang="en">
<head>
<meta charset="utf-8">
<title>Sol Rumbo Coaching Services — Letterhead</title>
<link rel="stylesheet" href="https://fonts.googleapis.com/css2?family=Source+Sans+3:wght@400;600&display=swap">
<style>
  :root {
    --paper: #ffffff;
    --ink: #3f3f3f;
    --brand-red: #c1272d;
    --brand-orange: #f39323;
    --corner-light: #efecea;
    --corner-dark: #d3ccc9;
  }
  html, body {
    margin: 0;
    padding: 0;
    overflow: hidden;
    background: var(--paper);
  }
  .letterhead {
    position: relative;
    width: 856px;
    height: 1200px;
    overflow: hidden;
    background: var(--paper);
    font-family: "Source Sans 3", sans-serif;
    color: var(--ink);
  }

  .corner-accent {
    position: absolute;
    background: linear-gradient(135deg, var(--corner-light), var(--corner-dark));
  }
  .corner-accent--top {
    top: 0;
    right: 0;
    width: 172px;
    height: 122px;
    clip-path: polygon(0 0, 100% 0, 100% 100%);
  }
  .corner-accent--bottom {
    bottom: 0;
    left: 0;
    width: 248px;
    height: 162px;
    clip-path: polygon(0 0, 0 100%, 100% 100%);
    background: linear-gradient(45deg, var(--corner-dark), var(--corner-light));
  }

  .brand {
    position: absolute;
    top: 27px;
    left: 48px;
    width: 196px;
    text-align: center;
  }
  .brand__dot {
    display: block;
    width: 66px;
    height: 66px;
    margin: 0 auto 8px;
    border-radius: 50%;
    background: var(--brand-orange);
  }
  .brand__name {
    margin: 0;
    font-weight: 600;
    color: var(--brand-red);
    line-height: 1;
  }
  .brand__name-main {
    display: block;
    font-size: 38px;
    letter-spacing: 0.5px;
  }
  .brand__name-sub {
    display: block;
    margin-top: 6px;
    font-size: 13px;
    letter-spacing: 2.6px;
    text-transform: uppercase;
  }

  .contact {
    position: absolute;
    top: 88px;
    left: 539px;
    margin: 0;
    font-size: 14px;
    line-height: 17px;
  }
  .contact__label { font-weight: 600; }

  .address {
    position: absolute;
    top: 1135px;
    left: 318px;
    width: 490px;
    margin: 0;
    font-size: 14px;
    line-height: 17px;
    text-align: center;
  }
  .address__label { font-weight: 600; }
</style>
</head>
<body>
<main class="letterhead">
  <div class="corner-accent corner-accent--top" role="img" aria-label="Decorative diagonal stripe pattern in warm greys"></div>

  <div class="brand">
    <span class="brand__dot" aria-hidden="true"></span>
    <p class="brand__name">
      <span class="brand__name-main">Sol Rumbo</span>
      <span class="brand__name-sub">Coaching Services</span>
    </p>
  </div>

  <p class="contact">
    <span class="contact__label">Email:</span> darsie@solrumbocoaching.example<br>
    <span class="contact__label">Web:</span> solrumbocoaching.example<br>
    <span class="contact__label">Mobile:</span> +555-413-7082
  </p>

  <div class="corner-accent corner-accent--bottom" role="img" aria-label="Decorative diagonal stripe pattern in warm greys"></div>

  <p class="address">
    <span class="address__label">Address:</span> 2140 Calle Mirasol, Suite 12, Lantern Bay, NJ 07000 · Sessions in person and online, Monday to Friday by appointment.
  </p>
</main>
</body>
</html>
```